Flyer für einen Pflegedienst
Zielgruppe
Wir sind ein Pflegedienst, unsere Zielgruppe sind alle Menschen die Unterstützung brauchen. Das sind im Hauptteil Senioren.
Aufgabenstellung
Der Flyer soll im DIN A5 Format designed sein. Der Print soll hochwertig sein. Wir möchten vor allem wohlhabendere Kunden damit ansprechen. Er soll die Kunden direkt packen, aber auch nicht zu viele Informationen beinhalten, die einen überfordern.

```html
<!DOCTYPE html>
<html lang="de">
<head>
<meta charset="utf-8">
<title>Pflege Halden – Flyer</title>
<link href="https://fonts.googleapis.com/css2?family=Fira+Sans:wght@600;700&family=Mulish:ital,wght@0,400;0,500;1,400&display=swap" rel="stylesheet">
<style>
  :root{
    --blue:#1672ae;
    --blue-dark:#0f5f97;
    --beige:#dccbb8;
    --paper:#fbfaf8;
    --ink:#2b2b2b;
    --frame:#8f8f8f;
    --white:#ffffff;
  }
  *{box-sizing:border-box;margin:0;padding:0}
  html,body{width:1200px;height:852px;overflow:hidden;background:var(--white)}
  body{position:relative;font-family:"Mulish",sans-serif;color:var(--ink)}
  .page{position:absolute;top:16px;width:580px;height:821px;background:var(--paper);border:2.5px solid var(--frame);overflow:hidden}
  .page--front{left:12px}
  .page--back{left:608px}
  .photo{position:absolute;left:0;top:0;width:100%}
  .page--front .photo{height:393px;background:linear-gradient(120deg,#e9e3da 0%,#cfc4b5 35%,#4a8fc4 55%,#d9d0c4 80%,#eee9e2 100%)}
  .page--back .photo{height:286px;background:linear-gradient(110deg,#e7e1d8 0%,#3f88c2 35%,#d8cfc3 60%,#b9bcc0 80%,#ece7df 100%)}
  .band-blue{position:absolute;left:0;width:100%;height:21px;background:var(--blue)}
  .band-beige{position:absolute;left:100px;right:0;height:14px;background:var(--beige)}
  .page--front .band-blue{top:393px}
  .page--front .band-beige{top:414px}
  .page--back .band-blue{top:286px}
  .page--back .band-beige{top:307px}
  .brand{position:absolute;color:var(--white);display:flex;align-items:center;gap:10px}
  .brand__dot{border:3px solid var(--white);border-radius:50%;flex:none}
  .brand__name{font-family:"Mulish",sans-serif;font-weight:500;line-height:1}
  .brand__tag{font-size:13px;font-weight:400;margin-top:6px}
  .page--front .brand{left:75px;top:288px}
  .page--front .brand__dot{width:72px;height:72px}
  .page--front .brand__name{font-size:40px}
  .page--back .brand{left:293px;top:205px}
  .page--back .brand__dot{width:56px;height:56px}
  .page--back .brand__name{font-size:30px}
  .page--back .brand__tag{font-size:10.5px;margin-top:4px}
  .heading{font-family:"Fira Sans",sans-serif;font-weight:600;color:var(--blue);font-size:18.5px;position:absolute;left:51px}
  .page--front .heading{top:459px}
  .page--back .heading{top:355px}
  .intro{position:absolute;left:51px;right:48px;font-size:15px;line-height:19.7px}
  .intro p+p{margin-top:19.7px}
  .intro{top:488px}
  em{font-style:italic}
  .services{position:absolute;left:51px;top:387px;right:40px}
  .service{margin-bottom:17px}
  .service h3{font-style:italic;font-weight:400;font-size:15.5px;margin-bottom:4px}
  .service li{list-style:none;position:relative;padding-left:24px;font-size:15.5px;line-height:19.7px}
  .service li::before{content:"";position:absolute;left:2px;top:7px;width:6px;height:6px;border-radius:50%;background:var(--ink)}
  .footer{position:absolute;left:0;bottom:0;width:100%;height:115px;background:var(--blue);color:var(--white)}
  .contact{position:absolute;font-size:14.5px;line-height:23.5px;top:26px}
  .contact--address{left:53px}
  .contact--reach{left:301px}
  .contact strong{font-weight:700;font-family:"Fira Sans",sans-serif;font-weight:600;padding-left:24px}
  .contact .row{display:flex;align-items:center;gap:8px}
  .contact .row.indent{padding-left:24px}
  .icon{width:15px;height:15px;flex:none;stroke:var(--white);fill:none;stroke-width:1.4}
  .steps{position:absolute;left:49px;top:10px;width:250px}
  .footer h4{font-family:"Fira Sans",sans-serif;font-weight:600;font-size:13px;margin-bottom:6px;letter-spacing:.2px}
  .steps li{list-style:none;position:relative;padding-left:24px;font-size:12.5px;line-height:16.6px}
  .steps li::before{content:"";position:absolute;left:2px;top:6px;width:4.5px;height:4.5px;border-radius:50%;background:var(--white)}
  .divider{position:absolute;left:315px;top:12px;width:1.5px;height:88px;background:var(--white)}
  .promise{position:absolute;left:330px;top:10px;width:210px;font-size:12.5px;line-height:16.6px}
</style>
</head>
<body>

<section class="page page--front">
  <div class="photo" role="img" aria-label="Foto: Pflegerin in blauer Dienstkleidung hält die Hände einer Seniorin auf dem Sofa"></div>
  <div class="brand">
    <span class="brand__dot"></span>
    <div>
      <div class="brand__name">Pflege Halden</div>
      <div class="brand__tag">Gemeinsam Leben, liebevoll Pflegen</div>
    </div>
  </div>
  <div class="band-blue"></div>
  <div class="band-beige"></div>

  <h2 class="heading">Gemeinsam leben, liebevoll pflegen</h2>
  <div class="intro">
    <p><em>Pflege Halden</em> - Wir sind Ihr zuverlässiger ambulanter Pflegedienst für Mülheim an der Ruhr, Süd-Duisburg, Süd- &amp; West-Essen, Süd-Oberhausen, Ratingen &amp; Lintorf.</p>
    <p>Mit dem Grundsatz <em>„Gemeinsam leben, liebevoll pflegen“</em> verpflichten wir uns, jedem Patienten nicht nur professionelle Pflege, sondern auch ein Gefühl von familiärer Geborgenheit und Respekt zu bieten. In dieser Atmosphäre des Vertrauens möchten wir unseren Patienten und ihren Familien Sicherheit und eine stetige Verbesserung der Lebensqualität bieten.</p>
  </div>

  <footer class="footer">
    <div class="contact contact--address">
      <div><strong>Pflege Halden</strong></div>
      <div class="row">
        <svg class="icon" viewBox="0 0 16 16"><path d="M2 8 8 2.5 14 8M3.5 7v6.5h9V7"/></svg>
        Lindenhofstraße 7b
      </div>
      <div class="row indent">45470 Mülheim an der Ruhr</div>
    </div>
    <div class="contact contact--reach">
      <div class="row">
        <svg class="icon" viewBox="0 0 16 16"><path d="M3 2.5l2.5-.5 1.5 3-1.5 1.2a8 8 0 0 0 4.3 4.3L11 9l3 1.5-.5 2.5c-6 .5-11-4.5-10.5-10.5z"/></svg>
        0208 - 55501230
      </div>
      <div class="row">
        <svg class="icon" viewBox="0 0 16 16"><circle cx="8" cy="8" r="6"/><path d="M2 8h12M8 2c-3 3.5-3 8.5 0 12M8 2c3 3.5 3 8.5 0 12"/></svg>
        www.pflegehalden.de
      </div>
      <div class="row">
        <svg class="icon" viewBox="0 0 16 16"><rect x="2" y="4" width="12" height="8.5"/><path d="M2 4l6 5 6-5"/></svg>
        info@pflegehalden.de
      </div>
    </div>
  </footer>
</section>

<section class="page page--back">
  <div class="photo" role="img" aria-label="Foto: Pflegerin reicht einem Senior auf dem Sofa ein Glas Wasser und eine Tablette"></div>
  <div class="brand">
    <span class="brand__dot"></span>
    <div>
      <div class="brand__name">Pflege Halden</div>
      <div class="brand__tag">Gemeinsam Leben, liebevoll Pflegen</div>
    </div>
  </div>
  <div class="band-blue"></div>
  <div class="band-beige"></div>

  <h2 class="heading">Das können wir für Sie tun:</h2>
  <div class="services">
    <div class="service">
      <h3>Behandlungspflege</h3>
      <ul>
        <li>Professionelle Wundversorgung und Verbandswechsel</li>
        <li>Zuverlässige Medikamentengabe und Injektionen</li>
        <li>Auf individuelle Bedürfnisse abgestimmte Pflege</li>
      </ul>
    </div>
    <div class="service">
      <h3>Grundpflege</h3>
      <ul>
        <li>Assistenz bei Routinen (Baden, Ankleiden und Körperpflege)</li>
        <li>Unterstützung bei Mobilität und Erhalt der Selbstständigkeit</li>
        <li>Hilfe bei Nahrungs- und Flüssigkeitsaufnahme</li>
      </ul>
    </div>
    <div class="service">
      <h3>Betreuung &amp; Hauswirtschaft</h3>
      <ul>
        <li>Unterstützung bei hauswirtschaftlichen Aufgaben</li>
        <li>Hilfe bei Einkäufen oder Behördengängen</li>
        <li>Gemeinsame Aktivitäten und sozialer Austausch</li>
      </ul>
    </div>
  </div>

  <footer class="footer">
    <div class="steps">
      <h4>So schnell kommt unser Pflegedienst:</h4>
      <ul>
        <li>Rufen Sie uns an: 0208 - 555 012 30</li>
        <li>Wir kommen bei Ihnen vorbei</li>
        <li>Sie erhalten ein Angebot</li>
        <li>Die Pflege beginnt am nächsten Tag</li>
      </ul>
    </div>
    <div class="divider"></div>
    <div class="promise">
      <h4>Sie liegen uns am Herzen.</h4>
      <p>Daher werden Patienten bei uns ohne lange Wartezeiten aufgenommen.</p>
    </div>
  </footer>
</section>

</body>
</html>
```